Creative design for PLW Businesscard!

We would like a creative business card for our company The Maple Workshop. We situated in Barcelona and setup software development teams for companies in Belgium, Holland.

Orange is related to Holland.
PLW means cool in Dutch

* An Overview / Background of the Business & Services
o Setup and manage developer teams in Barcelona for for companies
in Holland, Belgium.
* The Target Market / Audience you are trying to reach
o Companies in Holland searching for developers
* Design Specifics; any preferences or ideas for Style, Colour,
Imagery, etc
o Orange, professional, fancy
o The Maple Workshop (PLW) means cool , good, nice

Target Market(s)

Companies in Holland searching for developers

Industry/Entity Type

Business

Contact Information for Business Card

Company name: The Maple Workshop

Name: Joost ter Haarveld

Title: Managing director (not necessary)

Email: joost@themapleworkshop.es

web: www.themapleworkshop.es

Phone: (+34) 932 487 113

Mobile: (+34) 668 302 947

Font styles to use
Other font styles liked:
• Bookman Old Style or Rockwell

Requirements
Must have
• Setup and manage developer teams in Barcelona for for companies
• in Holland, Belgium.

```html
<!DOCTYPE html>
<html lang="en">
<head>
<meta charset="utf-8">
<title>The Maple Workshop – Business Card</title>
<link rel="stylesheet" href="https://fonts.googleapis.com/css2?family=Varela+Round&display=swap">
<style>
  :root {
    --orange: #e9580f;
    --blue: #2437a0;
    --ink: #2b2b2b;
    --paper: #ffffff;
    --backdrop: #e7e6e3;
    --text-font: "Varela Round", sans-serif;
  }
  * { box-sizing: border-box; margin: 0; padding: 0; }
  html, body {
    width: 1200px; height: 873px; overflow: hidden;
    background: var(--backdrop);
    font-family: var(--text-font);
  }
  .stage {
    position: relative; width: 1200px; height: 873px;
    display: flex; justify-content: center; align-items: center; gap: 80px;
  }
  .card {
    position: relative; width: 360px; height: 558px;
    background: var(--paper);
    box-shadow: 0 2px 6px rgba(0,0,0,.12);
    overflow: hidden;
  }
  /* Front */
  .front-top {
    height: 150px; display: flex; align-items: center; padding-left: 36px;
  }
  .wordmark {
    display: flex; align-items: center; gap: 10px;
    font-size: 44px; color: var(--ink); letter-spacing: 2px;
  }
  .wordmark-dot {
    width: 18px; height: 18px; border-radius: 50%; background: var(--orange);
  }
  .front-field {
    position: absolute; left: 0; right: 0; top: 150px; bottom: 0;
    background: var(--orange);
  }
  .pointer-icon {
    position: absolute; left: 232px; top: 186px; width: 28px; height: 32px;
  }
  .company-name {
    position: absolute; right: 28px; bottom: 34px;
    text-align: right; color: var(--blue);
    font-size: 27px; line-height: 1.08;
  }
  /* Back */
  .contact {
    position: absolute; left: 30px; top: 36px;
    font-size: 13.5px; line-height: 1.45; color: var(--blue);
  }
  .contact-name { color: var(--orange); }
  .contact-phones { margin-top: 26px; }
  .label { color: var(--orange); }
  .website {
    position: absolute; right: 22px; top: 150px;
    writing-mode: vertical-rl;
    font-size: 14px; letter-spacing: .5px; color: var(--orange);
  }
</style>
</head>
<body>
<main class="stage">
  <section class="card card-front">
    <div class="front-top">
      <div class="wordmark"><span>PLW</span><span class="wordmark-dot"></span></div>
    </div>
    <div class="front-field">
      <svg class="pointer-icon" viewBox="0 0 28 32" aria-hidden="true">
        <path d="M2 2 L2 26 L8 20 L13 30 L17 28 L12 18 L21 18 Z" fill="#ffffff"/>
      </svg>
      <p class="company-name">The<br>Maple<br>Workshop</p>
    </div>
  </section>

  <section class="card card-back">
    <div class="contact">
      <p class="contact-name">Joost ter Haarveld</p>
      <p class="contact-title">Managing Director</p>
      <p class="contact-email">joost@themapleworkshop.es</p>
      <div class="contact-phones">
        <p><span class="label">Phone:</span> (+34) 932 487 113</p>
        <p><span class="label">Mobile:</span> (+34) 668 302 947</p>
      </div>
    </div>
    <p class="website">www.themapleworkshop.es</p>
  </section>
</main>
</body>
</html>
```